RW Coatings

Interior and Exterior Painting. Stucco. Remodeling. Custom Builds. Disaster Repair.
Professional service, extraordinary quality.
Trellco Service Award Winner
RWcoatingsco.example

```html
<!DOCTYPE html>
<html lang="en">
<head>
<meta charset="utf-8">
<title>RW Coatings – Postcard</title>
<link rel="stylesheet" href="https://fonts.googleapis.com/css2?family=Fira+Sans+Extra+Condensed:ital,wght@1,700;1,800&family=Poppins:ital,wght@0,500;0,600;0,700;1,600&display=swap">
<style>
  :root {
    --forest: #3f5347;
    --beige: #e6dcc4;
    --sky: #4f8fd0;
    --sky-light: #b9d6ef;
    --wall: #e6c24a;
    --paving: #9a8f86;
    --award-red: #e8524a;
    --paper: #ffffff;
    --ink: #222222;
    --rule: #777777;
    --canvas: #dedede;
  }
  * { box-sizing: border-box; margin: 0; padding: 0; }
  html, body { width: 874px; height: 1200px; overflow: hidden; }
  body { background: var(--canvas); position: relative; font-family: "Poppins", sans-serif; }

  .card {
    position: absolute; left: 38px; width: 798px; height: 532px;
    background: var(--paper); overflow: hidden;
    box-shadow: 0 4px 10px rgba(0,0,0,.18);
  }
  .card--front { top: 50px; }
  .card--back { top: 618px; }

  .card__shapes { position: absolute; inset: 0; width: 100%; height: 100%; }

  /* front */
  .house-photo {
    position: absolute; inset: 0;
    background:
      linear-gradient(180deg, var(--sky) 0%, var(--sky-light) 28%, #d9c9a4 45%, var(--wall) 62%, #c9ad52 78%, var(--paving) 100%);
  }
  .headline {
    position: absolute; left: 32px; top: 26px;
    font-family: "Fira Sans Extra Condensed", sans-serif;
    font-style: italic; font-weight: 800;
    font-size: 60px; line-height: 54px; letter-spacing: -0.5px;
    color: var(--forest);
  }
  .service-list {
    position: absolute; left: 34px; top: 335px; list-style: none;
    font-weight: 600; font-style: italic; font-size: 22px; line-height: 28px;
    color: var(--paper);
  }
  .service-list li { position: relative; padding-left: 20px; }
  .service-list li::before {
    content: ""; position: absolute; left: 0; top: 11px;
    width: 8px; height: 8px; border-radius: 50%; background: var(--paper);
  }
  .service-list li.cont::before { display: none; }
  .brand {
    position: absolute; left: 282px; top: 290px;
    display: flex; align-items: center; gap: 10px;
  }
  .brand__dot { width: 40px; height: 40px; border-radius: 50%; background: var(--award-red); }
  .brand__name { font-weight: 700; font-size: 28px; color: var(--paper); }
  .award {
    position: absolute; left: 572px; top: 292px; width: 180px;
    display: flex; flex-direction: column; align-items: center; gap: 8px;
  }
  .award__badge { width: 120px; height: 90px; background: var(--award-red); }
  .award__caption {
    width: 180px; padding: 5px 8px; background: var(--paper);
    font-weight: 700; font-size: 14px; line-height: 17px; text-align: center;
    color: var(--forest);
  }
  .website {
    position: absolute; right: 32px; top: 474px;
    font-weight: 500; font-size: 24px; color: var(--ink);
  }

  /* back */
  .intro {
    position: absolute; left: 38px; top: 40px;
    font-weight: 600; font-size: 25px; line-height: 30px; color: var(--forest);
  }
  .stamp-box { position: absolute; left: 661px; top: 25px; width: 112px; height: 124px; border: 1px solid #444; }
  .address-lines { position: absolute; left: 507px; top: 289px; width: 266px; }
  .address-lines span { display: block; height: 1px; background: var(--rule); margin-bottom: 42px; }
  .painters-photo {
    position: absolute; left: 0; top: 165px; width: 400px; height: 292px;
    background:
      linear-gradient(90deg, rgba(255,255,255,0) 55%, #fff 100%),
      linear-gradient(180deg, #fff 0%, rgba(255,255,255,0) 30%),
      linear-gradient(100deg, var(--wall) 0%, #d8c27a 25%, #b8bcc4 50%, #d9c35a 70%, #eee 100%);
  }
  .call-label {
    position: absolute; left: 38px; top: 464px;
    font-family: "Fira Sans Extra Condensed", sans-serif; font-style: italic; font-weight: 700;
    font-size: 15px; color: var(--paper);
  }
  .phone { position: absolute; left: 38px; top: 480px; font-weight: 700; font-size: 31px; color: var(--paper); }
  .contact {
    position: absolute; right: 25px; top: 474px; text-align: right;
    font-weight: 500; font-size: 13px; line-height: 18px; color: var(--ink);
  }
</style>
</head>
<body>

<section class="card card--front">
  <div class="house-photo" role="img" aria-label="Photo of a yellow two-storey stucco house with a tiled roof and garage under a blue sky"></div>
  <svg class="card__shapes" viewBox="0 0 798 532" aria-hidden="true">
    <defs>
      <linearGradient id="beigeFade" x1="0" y1="0" x2="0" y2="1">
        <stop offset="0" stop-color="#e6dcc4" stop-opacity=".95"/>
        <stop offset=".8" stop-color="#e6dcc4" stop-opacity=".85"/>
        <stop offset="1" stop-color="#e6dcc4" stop-opacity=".4"/>
      </linearGradient>
    </defs>
    <polygon points="0,0 237,0 440,300 0,300" fill="url(#beigeFade)"/>
    <path d="M0,305 L240,305 Q280,305 300,330 L370,455 L452,532 L0,532 Z" fill="var(--forest)"/>
    <polygon points="370,455 798,455 798,532 452,532" fill="var(--paper)"/>
    <path d="M370,455 L452,532" stroke="rgba(0,0,0,.15)" stroke-width="3"/>
  </svg>
  <h1 class="headline">Professional<br>Service,<br>Extraordinary<br>Quality.</h1>
  <div class="brand">
    <span class="brand__dot"></span>
    <span class="brand__name">RW Coatings</span>
  </div>
  <div class="award">
    <div class="award__badge" role="img" aria-label="Service award badge"></div>
    <p class="award__caption">Trellco Service<br>Award Winner</p>
  </div>
  <ul class="service-list">
    <li>Interior &amp;</li>
    <li class="cont">Exterior Painting</li>
    <li>Stucco</li>
    <li>Remodeling</li>
    <li>Custom Builds</li>
    <li>Disaster Repair</li>
  </ul>
  <p class="website">RWcoatingsco.example</p>
</section>

<section class="card card--back">
  <div class="painters-photo" role="img" aria-label="Photo of two painters on a ladder rolling paint onto a yellow wall"></div>
  <p class="intro">With years of experience,<br>RW Coatings Co. delivers top-tier<br>craftsmanship and reliability<br>in every project.</p>
  <div class="stamp-box"></div>
  <div class="address-lines"><span></span><span></span><span></span><span></span></div>
  <svg class="card__shapes" viewBox="0 0 798 532" aria-hidden="true">
    <defs>
      <linearGradient id="bandShade" x1="0" y1="0" x2="0" y2="1">
        <stop offset="0" stop-color="#000" stop-opacity=".18"/>
        <stop offset="1" stop-color="#000" stop-opacity="0"/>
      </linearGradient>
    </defs>
    <rect x="0" y="451" width="798" height="8" fill="url(#bandShade)"/>
    <polygon points="0,457 385,457 455,532 0,532" fill="var(--forest)"/>
  </svg>
  <p class="call-label">Call Today for a Free Estimate!</p>
  <p class="phone">555.014.2290</p>
  <p class="contact">dana.rwcoatings@mail.example<br>www.rwcoatingsco.example</p>
</section>

</body>
</html>
```